Stonefield Crew Brochure = SCB $$$

this brochure will be used for a canvassing campaign (door to door) appointment setting

the campaign will be for homeowners that would like to do any kind of improvement to their house - home improvement
from EXT paint or roof repair all the way to kitchen and bathroom remodeling

we want to catch the prospect eye with the brochure and to educate our prospect about the different ways they could improve their house step by step to their dream house

Target Market(s)

Homeowners
anyone who would like to improve or fix any part of their house

Industry/Entity Type

Home Improvement

Contact Information for Business Card

the green roof house blueprints on one side
the Stonefield Crew logo on the other side

Font styles to use
Serif
Decorative

Colors
ffffff
886aae
9bcb3b
e6e6e6

Requirements
Must have
• this is a TRI-FOLD brochure
• call for action -- schedule your free estimate
• or any idea that will lead to set up an appointment with our specialist
• LOOK AT MY WEBSITE TO UNDERSTAND MORE WHAT I LIKE
• WWW.THESTONEFIELDCREWS-EXAMPLE.COM
• services:
• Kitchen Renovations
• Bathroom Renovations
• Modern Landscaping
• Additions + in-law quarters
• Exterior paint +interior paint
• wood replacement + stucco repair
• roof repair
• railling and glass work
Nice to have
• the pictures I have uploaded can use as an example but im open to other ideas...
• THERE IS NO SUBSTITUTE FOR QUALITY.
• the picture of the women in the kitchen--
• i enjoy making food and spending time in my new kitchen, to see my whole family sitting down to eat dinner together in our perfect little kitchen make me so happy
Should not have
• the 2 brochures i have uploaded are for example only

```html
<!DOCTYPE html>
<html lang="en">
<head>
<meta charset="utf-8">
<title>Stonefield Crew Tri-Fold Brochure</title>
<link rel="stylesheet" href="https://fonts.googleapis.com/css2?family=Cinzel:wght@500&family=Lato:wght@400;700&family=Libre+Baskerville:wght@400;700&family=Montserrat:wght@500;700;800&display=swap">
<style>
:root{
  --purple:#886aae;
  --green:#9bcb3b;
  --green-dark:#5fa12a;
  --light:#e6e6e6;
  --white:#ffffff;
  --ink:#333333;
  --charcoal:#1c1c1c;
  --stage:#d4d4d4;
}
*{margin:0;padding:0;box-sizing:border-box}
html,body{width:1200px;height:1200px;overflow:hidden;background:var(--stage)}
body{position:relative;font-family:"Lato",sans-serif;color:var(--ink)}
.sheet{position:absolute;left:240px;width:720px;height:555px;background:var(--white);overflow:hidden;box-shadow:0 4px 14px rgba(0,0,0,.25)}
.sheet--outside{top:25px}
.sheet--inside{top:620px}
.panel-shade{position:absolute;top:0;width:240px;height:555px}
.panel-shade--fold{background:linear-gradient(90deg,#fff 0%,#fff 70%,#ececec 100%)}
.panel-shade--mid{background:linear-gradient(90deg,#f1f1f1 0%,#fff 25%,#fff 100%)}
.abs{position:absolute}
.shapes{position:absolute;left:0;top:0;width:720px;height:555px}
.photo{position:absolute;border-radius:2px;box-shadow:0 1px 3px rgba(0,0,0,.25)}
.tag{position:absolute;display:flex;align-items:center;height:13px}
.tag-icon{width:17px;height:17px;border-radius:50%;background:var(--white);border:1.5px solid var(--purple);margin-right:-5px;z-index:1;display:flex;align-items:center;justify-content:center}
.tag-icon i{width:7px;height:7px;border-radius:50%;background:var(--purple)}
.tag-label{background:var(--purple);color:var(--white);font-size:8px;font-weight:700;line-height:12px;padding:0 5px 0 9px;border-radius:0 6px 6px 0;white-space:nowrap}
.section-title{font-family:"Montserrat",sans-serif;font-weight:700;font-size:10.5px;color:var(--purple)}
.body-copy{font-size:7.4px;line-height:9.7px;text-align:justify;color:#3a3a3a}
.logo{position:absolute;display:flex;align-items:center;gap:4px}
.logo-mark{border-radius:50%;background:var(--green-dark);border:2px solid var(--charcoal)}
.logo-name{font-family:"Cinzel",serif;font-weight:500;color:#4a4a4a;line-height:1}
.contact{position:absolute;left:240px;width:240px;text-align:center;font-size:8px;line-height:10.5px;color:#222}
.contact strong{font-weight:700}
.contact-icon{display:block;margin:0 auto 6px;width:14px;height:14px}
.cta{position:absolute;left:304px;top:404px;width:114px;height:114px;border-radius:50%;background:var(--white);border:5px solid var(--green);text-align:center;font-family:"Montserrat",sans-serif;display:flex;flex-direction:column;justify-content:center;line-height:1}
.cta-small{font-size:11px;font-weight:500;color:var(--purple)}
.cta-your{font-size:10px;font-weight:500;color:#777;margin:2px 0}
.cta-free{font-size:25px;font-weight:800;color:var(--green-dark)}
.cta-est{font-size:14px;font-weight:700;color:var(--purple);margin-top:1px}
.tagline{position:absolute;left:480px;top:416px;width:240px;text-align:center;font-family:"Libre Baskerville",serif;line-height:31px;white-space:nowrap}
.tagline-line{display:block;color:var(--white);font-size:21px;font-weight:400}
.tagline-key{display:block;color:var(--green);font-size:25px;font-weight:700}
.tagline-bold{display:block;color:var(--white);font-size:22px;font-weight:700}
.cover-url{position:absolute;left:480px;top:531px;width:240px;text-align:center;color:var(--white);font-size:8px;letter-spacing:.6px}
</style>
</head>
<body>

<section class="sheet sheet--outside">
  <div class="panel-shade panel-shade--fold" style="left:0"></div>
  <div class="panel-shade panel-shade--mid" style="left:240px"></div>

  <svg class="shapes" viewBox="0 0 720 555">
    <defs>
      <linearGradient id="roofTiles" x1="0" y1="0" x2="1" y2="1">
        <stop offset="0" stop-color="#3a62b0"/><stop offset=".45" stop-color="#c98a55"/><stop offset="1" stop-color="#d8744a"/>
      </linearGradient>
      <linearGradient id="houseFront" x1="0" y1="0" x2="0" y2="1">
        <stop offset="0" stop-color="#cfdbe6"/><stop offset=".5" stop-color="#e9ebea"/><stop offset="1" stop-color="#b9b6ae"/>
      </linearGradient>
      <linearGradient id="greenBand" x1="0" y1="0" x2="1" y2="0">
        <stop offset="0" stop-color="#5fa12a"/><stop offset=".5" stop-color="#9bcb3b"/><stop offset="1" stop-color="#5fa12a"/>
      </linearGradient>
    </defs>
    <g role="img" aria-label="Modern white two-storey house with palm trees, wide garage and front steps">
      <rect x="480" y="0" width="240" height="400" fill="url(#houseFront)"/>
    </g>
    <g role="img" aria-label="Roofer in hard hat hammering new tiles over blue underlayment">
      <polygon points="0,500 240,392 330,438 480,400 480,555 0,555" fill="url(#roofTiles)"/>
    </g>
    <polyline points="0,492 240,385 320,426" fill="none" stroke="#9a9a9a" stroke-width="6"/>
    <rect x="226" y="418" width="11" height="11" fill="#9bcb3b"/><rect x="239" y="418" width="11" height="11" fill="#9bcb3b"/>
    <rect x="226" y="431" width="11" height="11" fill="#9bcb3b"/><rect x="239" y="431" width="11" height="11" fill="#9bcb3b"/>
    <polygon points="480,398 599,350 720,406 720,555 480,555" fill="#1c1c1c"/>
    <polyline points="404,437 599,340 720,398" fill="none" stroke="url(#greenBand)" stroke-width="11"/>
  </svg>

  <div class="tag" style="left:19px;top:18px"><span class="tag-icon"><i></i></span><span class="tag-label">Roof repair</span></div>
  <div class="photo" role="img" aria-label="Roofer in safety vest laying blue underlayment on a tiled roof beside a brick chimney" style="left:23px;top:40px;width:200px;height:111px;background:linear-gradient(160deg,#cfe3f2 0%,#9fb7cc 45%,#3d63a8 65%,#c9805a 100%)"></div>
  <div class="tag" style="left:19px;top:178px"><span class="tag-icon"><i></i></span><span class="tag-label">Railling and glass work</span></div>
  <div class="photo" role="img" aria-label="Worker in white overalls installing a glass window behind protective plastic" style="left:23px;top:207px;width:200px;height:121px;background:linear-gradient(180deg,#d9d6cf 0%,#c3d3de 45%,#e9e5dc 75%,#6b6b6b 100%)"></div>

  <h2 class="section-title abs" style="left:262px;top:13px">ABOUT US</h2>
  <p class="body-copy abs" style="left:262px;top:32px;width:201px">We believe that every project deserves the same kind of attention, no matter if it's a one room remodel or a new build of a multimillion dollar structure. To us, quality is achieving the best results, with the highest-grade material, at the lowest cost to you. That is how we define quality and that is what you're getting with the Stonefield Crew. We never use sub-contractors or outsource our jobs.</p>

  <div class="logo" style="left:302px;top:142px">
    <span class="logo-mark" style="width:32px;height:32px"></span>
    <span class="logo-name" style="font-size:13px">STONEFIELD<br>CREW</span>
  </div>

  <div class="contact" style="top:199px">
    <svg class="contact-icon" viewBox="0 0 14 14"><circle cx="7" cy="7" r="7" fill="#886aae"/><path d="M3.5 7.2 7 4l3.5 3.2H9.5V10h-5V7.2z" fill="#fff"/></svg>
    <strong>The Stonefield Crew</strong><br>418 Larkmoor Ave. Unit #3<br>Fernhollow, CA 90000
  </div>
  <div class="contact" style="top:265px">
    <svg class="contact-icon" viewBox="0 0 14 14"><circle cx="7" cy="7" r="7" fill="#886aae"/><path d="M5 3.8c.4 0 .9 1.3.9 1.6 0 .4-.6.6-.5.9.3.8 1.1 1.7 1.9 2 .3.1.5-.5.9-.5.3 0 1.6.5 1.6.9 0 .6-.7 1.5-1.5 1.5C6 10.2 3.8 8 3.8 5.3c0-.8.6-1.5 1.2-1.5z" fill="#fff"/></svg>
    (555) 014-2290
  </div>
  <div class="contact" style="top:309px">
    <svg class="contact-icon" viewBox="0 0 14 14"><circle cx="7" cy="7" r="7" fill="#886aae"/><rect x="3.6" y="4.6" width="6.8" height="4.8" fill="#fff"/><path d="M3.6 4.6 7 7.3l3.4-2.7" stroke="#886aae" stroke-width=".8" fill="none"/></svg>
    hi@thestonefieldcrews-example.com
  </div>
  <div class="contact" style="top:352px">
    <svg class="contact-icon" viewBox="0 0 14 14"><circle cx="7" cy="7" r="7" fill="#886aae"/><circle cx="7" cy="7" r="3.6" fill="none" stroke="#fff" stroke-width=".9"/><path d="M3.4 7h7.2M7 3.4c-1.6 2.2-1.6 5 0 7.2M7 3.4c1.6 2.2 1.6 5 0 7.2" stroke="#fff" stroke-width=".8" fill="none"/></svg>
    www.thestonefieldcrews-example.com
  </div>

  <div class="logo" style="left:512px;top:28px">
    <span class="logo-mark" style="width:54px;height:54px"></span>
    <span class="logo-name" style="font-size:17px;color:#3c3c3c">STONEFIELD<br>CREW</span>
  </div>

  <div class="cta">
    <span class="cta-small">schedule</span>
    <span class="cta-your">YOUR</span>
    <span class="cta-free">FREE</span>
    <span class="cta-est">estimate</span>
  </div>

  <h1 class="tagline">
    <span class="tagline-line">THERE IS NO</span>
    <span class="tagline-key">SUBSTITUTE</span>
    <span class="tagline-bold">FOR QUALITY</span>
  </h1>
  <p class="cover-url">WWW.THESTONEFIELDCREWS-EXAMPLE.COM</p>
</section>

<section class="sheet sheet--inside">
  <div class="panel-shade panel-shade--fold" style="left:0"></div>
  <div class="panel-shade panel-shade--mid" style="left:240px"></div>
  <div class="panel-shade panel-shade--mid" style="left:480px"></div>

  <svg class="shapes" viewBox="0 0 720 555">
    <defs>
      <linearGradient id="kitchenScene" x1="0" y1="0" x2="1" y2="0">
        <stop offset="0" stop-color="#cfc6bc"/><stop offset=".4" stop-color="#e9e5df"/><stop offset=".7" stop-color="#b7a795"/><stop offset="1" stop-color="#d9d2c8"/>
      </linearGradient>
      <linearGradient id="greenBand2" x1="0" y1="0" x2="1" y2="0">
        <stop offset="0" stop-color="#5fa12a"/><stop offset=".6" stop-color="#9bcb3b"/><stop offset="1" stop-color="#5fa12a"/>
      </linearGradient>
    </defs>
    <g role="img" aria-label="Smiling woman holding a mug in a bright white kitchen while a handyman installs cabinets, beside a finished marble kitchen and a smiling contractor in a blue shirt">
      <polygon points="0,512 240,398 366,456 609,356 720,420 720,555 0,555" fill="url(#kitchenScene)"/>
      <rect x="570" y="400" width="150" height="155" fill="#3f78c4" opacity=".55"/>
    </g>
    <polyline points="0,505 240,391 300,418" fill="none" stroke="#9a9a9a" stroke-width="6"/>
    <rect x="226" y="424" width="11" height="11" fill="#9bcb3b"/><rect x="239" y="424" width="11" height="11" fill="#9bcb3b"/>
    <rect x="226" y="437" width="11" height="11" fill="#9bcb3b"/><rect x="239" y="437" width="11" height="11" fill="#9bcb3b"/>
    <polyline points="366,456 609,350 720,414" fill="none" stroke="url(#greenBand2)" stroke-width="11"/>
  </svg>

  <h2 class="section-title abs" style="left:19px;top:12px">SERVICES:</h2>
  <div class="tag" style="left:17px;top:40px"><span class="tag-icon"><i></i></span><span class="tag-label">Kitchen Renovations</span></div>
  <p class="body-copy abs" style="left:19px;top:58px;width:200px">There is a reason the Kitchen is called "The Heart of the Home." From bustling family breakfasts through baking misadventures covered in flour to soothing late-night conversations over tea, the Kitchen serves as the setting for the primary bonding moments in the home. Shouldn't your Kitchen invite your family in?</p>
  <div class="photo" role="img" aria-label="Modern kitchen with dark grey cabinets, wooden island and bar stools" style="left:19px;top:130px;width:200px;height:121px;background:linear-gradient(180deg,#eceae6 0%,#5d656b 40%,#b98755 75%,#8d6a48 100%)"></div>
  <div class="tag" style="left:17px;top:270px"><span class="tag-icon"><i></i></span><span class="tag-label">Bathroom Renovations</span></div>
  <p class="body-copy abs" style="left:19px;top:290px;width:200px">Everyone wants to relax after a long day in a Bathroom that serves as a high-end spa conveniently located in your home. Whether it's taking a steaming shower after a strenuous workout, or unwinding after a long day by soaking in a bubbly bathtub, your Bathroom should be a place of repose and rejuvenation. Let us help you relax.</p>

  <div class="tag" style="left:257px;top:18px"><span class="tag-icon"><i></i></span><span class="tag-label">Modern Landscaping</span></div>
  <p class="body-copy abs" style="left:259px;top:37px;width:200px">Want to be that neighbor–the one with the amazing lawn that everyone has to stare at before they continue on their way? One of our specialties is embracing California's dry climate to create a Drought-Tolerant Garden– a yard or lawn teeming with a colorful medley of low-maintenance succulents. Good for the planet and eye-catchingly beautiful– sounds like a win-win situation!</p>
  <div class="photo" role="img" aria-label="Landscapers in sun hats planting succulents beside a new paver path" style="left:262px;top:126px;width:198px;height:122px;background:linear-gradient(180deg,#e8e8e4 0%,#9c7c62 35%,#8a6b52 70%,#b9b3a8 100%)"></div>
  <div class="tag" style="left:257px;top:264px"><span class="tag-icon"><i></i></span><span class="tag-label">Additions + in-law quarters</span></div>
  <p class="body-copy abs" style="left:261px;top:284px;width:199px">Want to utilize the greatest potential of your premises? Whether it's building guest lodgings to rent out when your bills become overwhelming, or creating a cozy space for friends and family to stay while visiting, sometimes you just need to accommodate more people. A space completely separate from you, yet still yours. Shouldn't you get to benefit from the entirety of your property?</p>

  <div class="tag" style="left:497px;top:18px"><span class="tag-icon"><i></i></span><span class="tag-label">Exterior paint +interior paint</span></div>
  <div class="photo" role="img" aria-label="Painters in white rolling paint onto the walls and ceiling of a bright room" style="left:500px;top:39px;width:200px;height:86px;background:linear-gradient(180deg,#f3f3f1 0%,#dedcd6 60%,#a7a29a 100%)"></div>
  <div class="tag" style="left:497px;top:153px"><span class="tag-icon"><i></i></span><span class="tag-label">wood replacement + stucco repair</span></div>
  <div class="photo" role="img" aria-label="Evening patio under a wooden pergola with lounge seating and warm lights" style="left:500px;top:180px;width:200px;height:97px;background:linear-gradient(180deg,#2b3c74 0%,#6b4a3a 45%,#3b4a3a 75%,#1f2530 100%)"></div>

  <div class="logo" style="left:324px;top:378px">
    <span class="logo-mark" style="width:28px;height:28px"></span>
    <span class="logo-name" style="font-size:11px">STONEFIELD<br>CREW</span>
  </div>
</section>

</body>
</html>
```